Price list for young Relaxon clinic

I require a price list/Treatment menu for clinic

To include:
Logo
Address
Phone number
Website

List of services and Prices
Relaxon 1 area £100
Relaxon 2 areas £150
Relaxon 3 areas £200
Lip Enhancement 0.5ml £100
Lip Enhancement 1ml £200
Facial Fillers £200 per 1ml
Volumiq £450 per session (2 vials - must be bought as a course)
Non Surgical Face Lift (Thread Lift) £600 per area
Skin Press Full Face £250
Skin Press Small Per Small Area £100
Cryo Therapy £60
Chemical Peel Light Peel and Microdermabrasion £85
Chemical Peel Deep Peel £150
Consultation £30 redeemable against service
Relaxon Top Up Relaxon £50 (must be within 2 weeks of 1st treatment)
Filler Top Up £100 (must be within 2 weeks of 1st appointment)

Open Hours
Updates

Company Name: HVM Address: 482 Pellbrook Road, 6 Warnford High Street, KT4 3JQ Phone: 0208 947 2186 Website: www.hollyvanmereaesthetics.co.uk

Please add more colour

Needs to be much cleaner and simpler Front page to include logo and price list Back page to inculde open hours and contact information including google map. Please no images with needles. Images of lips and faces are good, but try not to crowd copy on the pagei. No copy on top of images. White, grey, black and reds are good on colouring.

Target Market(s)

young market ages 22-45 years old mainly female
modern

Industry/Entity Type

Clinic

Number of Pages Required

4 page

Requirements
Must have
• Logo - logo must be in colour grey/silver
• Address (small map?)
• Phone number
• Web address
• Services
• Open hours
• Prices
• Images

```html
<!DOCTYPE html>
<html lang="en">
<head>
<meta charset="utf-8">
<title>Holly Vanmere Aesthetics – Treatment Brochure</title>
<link rel="stylesheet" href="https://fonts.googleapis.com/css2?family=Cinzel:wght@400;600&family=Parisienne&family=Montserrat:wght@300;400;500&family=Lato:wght@400;700&display=swap">
<style>
  :root{
    --silver-light:#f4f4f4;
    --silver:#d6d6d6;
    --silver-mid:#bdbdbd;
    --grey-dark:#8a8a8a;
    --grey-text:#9c9c9c;
    --ink:#5e5e5e;
    --rose:#c48f93;
    --rose-deep:#a8666c;
    --white:#ffffff;
    --skin-light:#d9ad94;
    --hair:#3a2a22;
    --map:#e6e3dd;
  }
  *{box-sizing:border-box;margin:0;padding:0}
  html,body{width:1200px;height:847px;overflow:hidden;background:var(--silver)}
  .spread{display:flex;width:1200px;height:847px}
  .page{position:relative;width:600px;height:847px;overflow:hidden}

  /* back page */
  .page--back{background:linear-gradient(180deg,var(--silver-light) 0%,#e2e2e2 40%,var(--silver) 100%)}
  .tagline{position:absolute;top:38px;left:0;width:600px;text-align:center;color:var(--grey-text)}
  .tagline__lead{font-family:'Montserrat',sans-serif;font-weight:300;font-size:14px;letter-spacing:14px}
  .tagline__script{font-family:'Parisienne',cursive;font-size:40px;line-height:46px}
  .timeline{position:absolute;top:188px;left:0;width:600px;display:flex}
  .timeline__step{flex:1;border-right:2px solid var(--white)}
  .timeline__step:last-child{border-right:0}
  .timeline__label{height:30px;background:linear-gradient(180deg,#c9c9c9,#a9a9a9);color:var(--white);font-family:'Montserrat',sans-serif;font-size:13px;text-align:center;line-height:27px;border-top:3px solid var(--rose)}
  .timeline__photo{height:250px;background:linear-gradient(180deg,#5a3d30 0%,#b07d66 30%,#c99a82 60%,#a4705b 100%)}
  .contact{position:absolute;top:468px;left:0;width:600px;height:166px;background:var(--rose);color:var(--white);text-align:center;padding-top:26px}
  .contact__title{font-family:'Montserrat',sans-serif;font-weight:400;font-size:22px;letter-spacing:1px;text-transform:uppercase}
  .contact__body{font-family:'Montserrat',sans-serif;font-weight:300;font-size:13px;line-height:19px;text-transform:uppercase;margin-top:8px;letter-spacing:.5px}
  .contact__details{position:absolute;top:642px;left:0;width:600px;text-align:center;font-family:'Lato',sans-serif;font-size:10.5px;line-height:15px;color:var(--grey-text)}
  .hours{position:absolute;top:690px;left:22px;width:118px;font-family:'Montserrat',sans-serif;color:var(--ink)}
  .hours__title{font-size:11px;font-weight:500;letter-spacing:1.5px;color:var(--rose-deep);margin-bottom:6px}
  .hours__row{display:flex;justify-content:space-between;font-size:10px;line-height:17px}
  .map{position:absolute;top:682px;left:150px;width:360px;height:152px;background:var(--map);border:1px solid #cfcac2}

  /* front page */
  .page--front{background:var(--white)}
  .brand{position:absolute;top:20px;left:0;width:600px;display:flex;flex-direction:column;align-items:center}
  .brand__mark{width:70px;height:70px;border-radius:50%;background:var(--grey-dark);color:var(--white);font-family:'Cinzel',serif;font-size:20px;display:flex;align-items:center;justify-content:center}
  .brand__name{font-family:'Cinzel',serif;font-size:16px;letter-spacing:2px;color:var(--grey-dark);margin-top:8px;text-align:center;line-height:20px}
  .rule{position:absolute;left:0;width:600px;height:5px;background:var(--silver-mid)}
  .rule--top{top:142px}
  .hero{position:absolute;top:156px;left:60px;width:470px;height:356px;background:linear-gradient(180deg,#4a3127 0%,#c89377 35%,#e0b49c 65%,#d6a88f 100%)}
  .results{position:absolute;top:518px;left:0;width:600px;height:134px;background:linear-gradient(180deg,#e9e9e9,#d3d3d3);display:flex;gap:18px;justify-content:center;align-items:center}
  .results__photo{width:165px;height:108px;background:linear-gradient(90deg,#c79a84,#e0b8a2 50%,#c79a84)}
  .prices{position:absolute;top:662px;left:30px;width:540px;font-family:'Montserrat',sans-serif;color:var(--ink)}
  .prices__title{font-size:12px;font-weight:500;letter-spacing:3px;color:var(--rose-deep);text-align:center;margin-bottom:6px}
  .prices__list{list-style:none;columns:2;column-gap:28px}
  .prices__item{display:flex;justify-content:space-between;font-size:9.5px;line-height:19px;border-bottom:1px solid #ececec;break-inside:avoid}
  .prices__item span:last-child{color:var(--rose-deep);font-weight:500;white-space:nowrap;padding-left:6px}
</style>
</head>
<body>
<main class="spread">
  <section class="page page--back">
    <div class="tagline">
      <p class="tagline__lead">ACHIEVE</p>
      <p class="tagline__script">a fresh and<br>beautiful you</p>
    </div>
    <div class="timeline">
      <div class="timeline__step"><p class="timeline__label">BEFORE</p><div class="timeline__photo" role="img" aria-label="Client portrait before treatment"></div></div>
      <div class="timeline__step"><p class="timeline__label">DAY 7</p><div class="timeline__photo" role="img" aria-label="Client portrait seven days after treatment"></div></div>
      <div class="timeline__step"><p class="timeline__label">DAY 90</p><div class="timeline__photo" role="img" aria-label="Client portrait ninety days after treatment"></div></div>
      <div class="timeline__step"><p class="timeline__label">DAY 120</p><div class="timeline__photo" role="img" aria-label="Client portrait one hundred and twenty days after treatment"></div></div>
    </div>
    <div class="contact">
      <h2 class="contact__title">Contact us today</h2>
      <p class="contact__body">to book a cosmetic surgery consultation<br>with Mr Daniel Ashcombe<br>(voted one of Salonette 2015's<br>top plastic surgeons).</p>
    </div>
    <div class="contact__details">
      <p>482 Pellbrook Road, 6 Warnford High Street, KT4 3JQ</p>
      <p>Phone: 0208 947 2186 | Email: hvmwarnfordbookings@mailbox.co.uk | www.hollyvanmereaesthetics.co.uk</p>
    </div>
    <div class="hours">
      <p class="hours__title">OPEN HOURS</p>
      <p class="hours__row"><span>Mon – Fri</span><span>9 – 7</span></p>
      <p class="hours__row"><span>Saturday</span><span>10 – 5</span></p>
      <p class="hours__row"><span>Sunday</span><span>Closed</span></p>
    </div>
    <div class="map" role="img" aria-label="Street map showing the clinic location on Warnford High Street"></div>
  </section>

  <section class="page page--front">
    <header class="brand">
      <div class="brand__mark">HVM</div>
      <p class="brand__name">HOLLY VANMERE<br>AESTHETICS</p>
    </header>
    <div class="rule rule--top"></div>
    <div class="hero" role="img" aria-label="Portrait of a woman with treatment areas marked"></div>
    <div class="results">
      <div class="results__photo" role="img" aria-label="Before and after eye area result"></div>
      <div class="results__photo" role="img" aria-label="Before and after forehead result"></div>
      <div class="results__photo" role="img" aria-label="Before and after under-eye result"></div>
    </div>
    <div class="prices">
      <h2 class="prices__title">TREATMENTS &amp; PRICES</h2>
      <ul class="prices__list">
        <li class="prices__item"><span>Relaxon 1 / 2 / 3 areas</span><span>£100 / £150 / £200</span></li>
        <li class="prices__item"><span>Lip Enhancement 0.5ml / 1ml</span><span>£100 / £200</span></li>
        <li class="prices__item"><span>Facial Fillers (per 1ml)</span><span>£200</span></li>
        <li class="prices__item"><span>Volumiq (2 vials, course)</span><span>£450</span></li>
        <li class="prices__item"><span>Thread Lift (per area)</span><span>£600</span></li>
        <li class="prices__item"><span>Skin Press Full Face / Small Area</span><span>£250 / £100</span></li>
        <li class="prices__item"><span>Cryo Therapy</span><span>£60</span></li>
        <li class="prices__item"><span>Light Peel &amp; Microdermabrasion</span><span>£85</span></li>
        <li class="prices__item"><span>Chemical Deep Peel</span><span>£150</span></li>
        <li class="prices__item"><span>Consultation (redeemable)</span><span>£30</span></li>
        <li class="prices__item"><span>Relaxon Top Up (within 2 wks)</span><span>£50</span></li>
        <li class="prices__item"><span>Filler Top Up (within 2 wks)</span><span>£100</span></li>
      </ul>
    </div>
  </section>
</main>
</body>
</html>
```